Business Intelligence Dashboard header

We are a top 10 cancer treatment clinic. Our analytics teams (Corporate Finance, Financial Analytics, and Clinical Analytics) are searching for a great graphic to show our business partners the value of our business intelligence products. We are hoping to convey that we are tech-savvy, supportive to our patients and mission of saving lives, valuable, forward-thinking, agile, supportive, and friendly.

This header will be placed at the top of each data visualization ('viz') that we create. We would like a design that is in-line with our company branding, simple, elegant, and striking. We primarily create headers that are between 800 and 1300 pixels across (800 and 1300 being the most common) and between 60 and 80 pixels high (76 being our current header height in px, but we are open to slight deviation.) The type of data visualizations this will sit atop (everything we produce, but just a few examples) will be things like patient safety, clinic utilization, appointment volumes, provider scorecards, and many more. I've included our current header, and a header I saw and liked (although I think it could have been a bit cooler.)

I'm open to ideas, feedback, and your opinion as a designer to come up with something amazing. You can find our website at https://www.brightharborhealth.org/
Googling our business shows our main clinic (with the rounded front) https://www.findwell.com/search?q=brightharbor+oncology+partners&source=lnms&tbm=isch&sa=X&ved=0ahUKEwjjws22xuLXAhVM5mMKHb82CpQQ_AUIDCgD&biw=1995&bih=916

We are open to stock images.

Requirements
Must have
• A place to write in a dashboard title (we will use our own BI-native object to float over the top of this banner)
Nice to have
• We would like a place/icon to differentiate between work products coming out of Clinical Analytics/Financial Analytics/Corporate Finance. We're fine with it being on 2 lines, or simply designing an icon to differentiate. We could use smaller text underneath the dashboard title (see must haves), an icon for each of the 3 teams, or a space in the header to write in the team ourselves. The team names should be of limited significance on the header. The star of the show will be the dashboard title (just leave an area for it) where the team names should be of less significance (off to the side, under the title in smaller font, etc)

```html
<!DOCTYPE html>
<html lang="en">
<head>
<meta charset="utf-8">
<title>Dashboard Header</title>
<link href="https://fonts.googleapis.com/css2?family=Source+Sans+3:wght@400;700&display=swap" rel="stylesheet">
<style>
  :root {
    --band: #78706c;
    --band-light: #8a827e;
    --accent: #f5c12e;
    --accent-soft: #f8d56a;
    --ink-light: #ffffff;
    --rule: rgba(255, 255, 255, 0.75);
  }
  html, body {
    margin: 0;
    padding: 0;
    width: 1200px;
    height: 120px;
    overflow: hidden;
    background: var(--band);
  }
  .header {
    position: relative;
    width: 1200px;
    height: 120px;
    background: radial-gradient(ellipse at 60% 40%, var(--band-light) 0%, var(--band) 70%);
    font-family: "Source Sans 3", "Helvetica Neue", Arial, sans-serif;
    color: var(--ink-light);
    overflow: hidden;
  }
  .texture {
    position: absolute;
    inset: 0;
    background: radial-gradient(circle at 30% 20%, rgba(255,255,255,0.06), transparent 40%),
                radial-gradient(circle at 80% 70%, rgba(255,255,255,0.05), transparent 35%);
  }
  .accent-left {
    position: absolute;
    left: 0; top: 0;
    width: 72px; height: 120px;
    background: linear-gradient(90deg, rgba(245,193,46,0.85) 0%, rgba(245,193,46,0.35) 60%, rgba(245,193,46,0) 100%);
  }
  .accent-right {
    position: absolute;
    right: 0; top: 0;
    width: 160px; height: 120px;
    background: linear-gradient(270deg, rgba(245,193,46,0.9) 0%, rgba(248,213,106,0.45) 60%, rgba(245,193,46,0) 100%);
  }
  .brand-name {
    position: absolute;
    left: 111px;
    top: 17px;
    margin: 0;
    font-size: 20px;
    line-height: 26px;
    font-weight: 700;
    color: var(--ink-light);
  }
  .divider {
    position: absolute;
    left: 271px;
    top: 18px;
    width: 1px;
    height: 84px;
    background: var(--rule);
  }
  .team-badge {
    position: absolute;
    left: 295px;
    top: 36px;
    width: 49px;
    height: 49px;
  }
  .dashboard-title {
    position: absolute;
    left: 357px;
    top: 31px;
    margin: 0;
    font-size: 25px;
    font-weight: 700;
    line-height: 30px;
  }
  .team-name {
    position: absolute;
    left: 357px;
    top: 63px;
    margin: 0;
    font-size: 21px;
    font-weight: 400;
    line-height: 26px;
  }
</style>
</head>
<body>
  <header class="header">
    <div class="texture" role="img" aria-label="Faint network pattern of connected nodes"></div>
    <div class="accent-left" role="img" aria-label="Yellow honeycomb accent cluster"></div>
    <div class="accent-right" role="img" aria-label="Yellow honeycomb accent cluster with plus marks"></div>

    <p class="brand-name">Bright<br>Harbor<br>Health</p>

    <div class="divider"></div>

    <svg class="team-badge" viewBox="0 0 49 49" aria-hidden="true">
      <rect x="0" y="0" width="49" height="49" rx="3" fill="var(--accent)"/>
      <circle cx="24.5" cy="24.5" r="18" fill="#ffffff"/>
    </svg>

    <h1 class="dashboard-title">Dashboard Title</h1>
    <p class="team-name">Team Name</p>
  </header>
</body>
</html>
```